Business card/Stationary for mobile ultrasound company
Corvin Ultrasound Services, LLC
Business card/Stationary for mobile ultrasound company -
Creative Brief
Use specific fonts
can use a combination of fonts similar to logo
Professional
Tessa Quillon RDMS, RVT, RCS
Owner
P.O. Box 482 Artesia, NM 88211-0482
4quillons@mailnest.example
I am currently getting a website designed so i will add a web address and an updated email address specifically for the business. I am torn as to use a one sided or 2 sided card. So im open. I would rather not have the address on the card. Thanks
Innovative mobile technology focused on improving the QUALITY of patient care. (The wording can change but along this idea)

```html
<!DOCTYPE html>
<html lang="en">
<head>
<meta charset="utf-8">
<title>Corvin Ultrasound Services – Business Card</title>
<link rel="stylesheet" href="https://fonts.googleapis.com/css2?family=Open+Sans:ital,wght@0,400;0,600;1,700&display=swap">
<style>
  :root {
    --backdrop: #d9d9d9;
    --card: #0b0b0b;
    --ink: #ffffff;
    --ink-soft: #e6e6e6;
    --olive: #7e7c46;
    --rule: #8a8a8a;
  }
  * { box-sizing: border-box; margin: 0; padding: 0; }
  html, body {
    width: 1200px;
    height: 780px;
    overflow: hidden;
    background: var(--backdrop);
    font-family: "Open Sans", Arial, sans-serif;
  }
  .business-card {
    position: absolute;
    left: 110px;
    top: 120px;
    width: 980px;
    height: 540px;
    background: var(--card);
    border-radius: 34px;
    color: var(--ink);
  }
  .edge-tab {
    position: absolute;
    top: 195px;
    width: 22px;
    height: 150px;
    background: var(--olive);
    border-radius: 6px;
  }
  .edge-tab--left { left: -6px; }
  .edge-tab--right { right: -6px; }

  .brand {
    position: absolute;
    left: 70px;
    top: 205px;
    width: 330px;
    text-align: center;
    font-weight: 600;
    color: var(--ink);
  }
  .brand-name {
    display: block;
    font-size: 64px;
    line-height: 1;
    letter-spacing: 1px;
  }
  .brand-sub {
    display: block;
    margin-top: 10px;
    font-size: 21px;
    line-height: 1.2;
  }

  .divider {
    position: absolute;
    left: 430px;
    top: 70px;
    width: 1px;
    height: 400px;
    background: var(--rule);
  }

  .contact {
    position: absolute;
    left: 466px;
    top: 66px;
    width: 460px;
  }
  .contact-name {
    font-size: 25px;
    font-weight: 700;
    font-style: italic;
    line-height: 1.3;
  }
  .contact-role {
    font-size: 22px;
    font-weight: 400;
    margin-top: 6px;
  }
  .contact-address {
    margin-top: 84px;
    font-size: 19px;
    line-height: 1.35;
    color: var(--ink-soft);
    font-style: normal;
  }
  .contact-line {
    display: flex;
    align-items: center;
    gap: 14px;
    font-size: 19px;
    color: var(--ink-soft);
  }
  .contact-line--phone { margin-top: 38px; }
  .contact-line--email { margin-top: 18px; }
  .contact-icon {
    width: 20px;
    height: 20px;
    flex: none;
  }
  .at-mark {
    width: 20px;
    text-align: center;
    font-weight: 600;
    font-size: 21px;
    color: var(--ink);
  }
</style>
</head>
<body>
  <main class="business-card">
    <span class="edge-tab edge-tab--left"></span>
    <span class="edge-tab edge-tab--right"></span>

    <div class="brand">
      <span class="brand-name">Corvin</span>
      <span class="brand-sub">Ultrasound Services, LLC</span>
    </div>

    <span class="divider"></span>

    <section class="contact">
      <h1 class="contact-name">Tessa Quillon RDMS, RVT, RCS</h1>
      <p class="contact-role">Owner</p>
      <address class="contact-address">
        P.O. Box 482<br>
        Artesia, NM 88211-0482
      </address>
      <p class="contact-line contact-line--phone">
        <svg class="contact-icon" viewBox="0 0 24 24" aria-hidden="true">
          <path fill="#ffffff" d="M6.6 10.8a15.1 15.1 0 0 0 6.6 6.6l2.2-2.2c.3-.3.7-.4 1-.2 1.1.4 2.3.6 3.6.6.6 0 1 .4 1 1V20c0 .6-.4 1-1 1A17 17 0 0 1 3 4c0-.6.4-1 1-1h3.5c.6 0 1 .4 1 1 0 1.3.2 2.5.6 3.6.1.3 0 .7-.2 1z"/>
        </svg>
        575-555-0142
      </p>
      <p class="contact-line contact-line--email">
        <span class="at-mark">@</span>
        4quillons@mailnest.example
      </p>
    </section>
  </main>
</body>
</html>
```